New Business Cards for Torvin Group

We need a new Business Card to compliment our new logo. We are a vibrant design, manufacture and install business providing recreation areas, public parks and Municipal spaces. We want business cards that are classy, modern and clean.

We have recently changed our logo, and are celebrating our 40th anniversary. We want business cards with a new modern design to reflect our status.

Target Market(s)

Customers

Contact Information for Business Card

We need all the details of our 3 offices as per the business card attached. Please disregard the old logo on the business card, the other three files show our new logo.

Requirements
Must have
• All info as per attached business card but with new logo.
Nice to have

```html
<!DOCTYPE html>
<html lang="en">
<head>
<meta charset="utf-8">
<title>Torvin Group – Business Card</title>
<link rel="stylesheet" href="https://fonts.googleapis.com/css2?family=Open+Sans:wght@400;600;700&display=swap">
<style>
  :root {
    --brand-red: #e8343b;
    --charcoal: #4a4a4f;
    --ink: #3b3b3f;
    --paper: #ffffff;
    --stage: #2e2e31;
    --rule: #c9c9cc;
  }
  * { box-sizing: border-box; margin: 0; padding: 0; }
  html, body { width: 1200px; height: 866px; overflow: hidden; }
  body {
    background: var(--stage);
    font-family: "Open Sans", Arial, sans-serif;
    position: relative;
  }
  .card {
    position: absolute;
    left: 267px;
    width: 665px;
    height: 380px;
    overflow: hidden;
    box-shadow: 0 10px 24px rgba(0,0,0,.45);
  }
  .card--front { top: 36px; background: var(--paper); }
  .card--back { top: 450px; background: var(--brand-red); color: var(--paper); }

  /* front */
  .brand {
    position: absolute; left: 70px; top: 120px;
    display: flex; align-items: center; gap: 16px;
  }
  .brand__dot { width: 64px; height: 64px; border-radius: 50%; background: var(--brand-red); flex: none; }
  .brand__name {
    font-weight: 700; font-size: 30px; line-height: 32px; color: var(--charcoal);
    letter-spacing: 1px; text-transform: uppercase;
  }
  .brand__name span { display: block; }
  .divider {
    position: absolute; left: 332px; top: 100px; width: 1px; height: 150px; background: var(--rule);
  }
  .person { position: absolute; left: 364px; top: 112px; }
  .person__name {
    font-weight: 700; font-size: 24px; color: var(--brand-red); letter-spacing: .5px;
    text-transform: uppercase; line-height: 1.1;
  }
  .person__role { font-size: 15px; color: var(--ink); margin-top: 2px; }
  .contact { list-style: none; margin-top: 18px; }
  .contact li {
    display: flex; align-items: center; gap: 10px;
    font-size: 14px; color: var(--ink); line-height: 22px;
  }
  .contact svg { width: 13px; height: 13px; flex: none; }
  .front-band { position: absolute; left: 0; bottom: 0; width: 665px; height: 34px; }

  /* back */
  .office { position: absolute; font-size: 14px; line-height: 20px; }
  .office__title { font-weight: 700; font-size: 16px; text-transform: uppercase; margin-bottom: 3px; letter-spacing: .3px; }
  .office--head { left: 330px; top: 44px; }
  .office--dubai { left: 44px; top: 140px; }
  .office--qatar { left: 330px; top: 226px; }
</style>
</head>
<body>
  <section class="card card--front" aria-label="Business card front">
    <div class="brand">
      <span class="brand__dot"></span>
      <p class="brand__name"><span>Torvin</span><span>Group</span></p>
    </div>
    <div class="divider"></div>
    <div class="person">
      <h1 class="person__name">Mara Velkoni</h1>
      <p class="person__role">Managing Partner</p>
      <ul class="contact">
        <li><svg viewBox="0 0 16 16"><path fill="var(--brand-red)" d="M3 1h3l1.5 4-2 1.2a9 9 0 0 0 4.3 4.3L11 8.5l4 1.5v3c0 1-1 2-2 2A12 12 0 0 1 1 3c0-1 1-2 2-2z"/></svg>+971 (0)50 555 0148</li>
        <li><svg viewBox="0 0 16 16"><rect x="1" y="3" width="14" height="10" fill="var(--brand-red)"/><path d="M1.5 3.5l6.5 5.5 6.5-5.5" fill="none" stroke="#fff" stroke-width="1.3"/></svg>mara@torvingroup.com</li>
        <li><svg viewBox="0 0 16 16"><circle cx="8" cy="8" r="7" fill="var(--brand-red)"/></svg>www.torvingroup.com</li>
      </ul>
    </div>
    <svg class="front-band" viewBox="0 0 665 34" preserveAspectRatio="none" aria-hidden="true">
      <polygon points="0,0 275,0 283,34 0,34" fill="var(--charcoal)"/>
      <polygon points="285,12 665,12 665,34 290,34" fill="var(--brand-red)"/>
    </svg>
  </section>

  <section class="card card--back" aria-label="Business card back">
    <div class="office office--head">
      <h2 class="office__title">Head Office</h2>
      <p>P.O.Box:10482 Abu Dhabi, U.A.E.</p>
      <p>P : +971 (0)2 555 0172</p>
      <p>F : +971 (0)2 555 0173</p>
      <p>E : sales@torvingroup.com</p>
    </div>
    <div class="office office--dubai">
      <h2 class="office__title">Dubai Office</h2>
      <p>P.O.Box:20317 Dubai, U.A.E.</p>
      <p>P : +971 (0)4 555 0136</p>
      <p>F : +971 (0)4 555 0137</p>
      <p>E : sales@torvingroup.com</p>
    </div>
    <div class="office office--qatar">
      <h2 class="office__title">Qatar Office</h2>
      <p>P.O.Box:30921 Doha, Qatar</p>
      <p>P : +974 4555 0190</p>
      <p>F : +974 4555 0191</p>
      <p>E : sales@torvingroup.com</p>
    </div>
  </section>
</body>
</html>
```